Security Consulting firm needs an ad design

We need a 3.375” x 4.875” ad design for our core services. The ad should include the company logo and the content from the first half of the attached sample JPG (Without the sentence under the title but including the description for the Plan - Design - Deploy - Manage and the titles ) as well as the following corporate information:
www.harborlanepartners.us
82 Morrow Ave. Suite 615, Alder Ridge, NJ 07413
PHONE 888-416-2057 / EMAIL info@harborlanepartners.us
The design should incorporate the same blue color that is in our logo and the font Raleway. Also - please use the same icons that are in the sample JPG - they can also be extracted from the attached indesign file.
The ad is to be publish in print and digital issue.
Please provide with all source files as well as a hi-res PDF using press quality or similar PDF settings.
- Raleway

```html
<!DOCTYPE html>
<html lang="en">
<head>
<meta charset="utf-8">
<title>Harbor Lane Partners – Creating Secure Environments</title>
<link href="https://fonts.googleapis.com/css2?family=Raleway:wght@300;400;700;800&family=Montserrat:wght@400;600;700&display=swap" rel="stylesheet">
<style>
  :root {
    --brand-blue: #2f78bb;
    --ink-dark: #303031;
    --band-light: #e8f0f8;
    --white: #ffffff;
    --page-bg: #f2f2f2;
    --text-grey: #3a3a3a;
  }
  * { margin: 0; padding: 0; box-sizing: border-box; }
  html, body { width: 990px; height: 1200px; overflow: hidden; background: var(--page-bg); }
  .ad {
    position: absolute; left: 79px; top: 0;
    width: 832px; height: 1200px; overflow: hidden;
    font-family: "Raleway", sans-serif; color: var(--white);
  }
  .ad-shapes { position: absolute; inset: 0; }
  .brand { position: absolute; left: 62px; top: 78px; display: flex; align-items: center; gap: 12px; }
  .brand-dot { width: 34px; height: 34px; border-radius: 50%; background: var(--white); }
  .brand-name { font-weight: 700; font-size: 34px; letter-spacing: 0.5px; color: var(--white); }
  .website {
    position: absolute; left: 512px; top: 66px; font-family: "Montserrat", sans-serif;
    font-weight: 600; font-size: 13.5px; letter-spacing: 1.6px; display: flex; align-items: center; gap: 6px;
  }
  .headline-rule { position: absolute; left: 62px; top: 587px; width: 4px; height: 226px; background: var(--white); border-radius: 2px; }
  .headline { position: absolute; left: 90px; top: 588px; text-transform: uppercase; line-height: 1; }
  .headline .lead { display: block; font-weight: 300; font-size: 55px; letter-spacing: 0.5px; }
  .headline .key { display: block; font-weight: 800; font-size: 108px; margin-top: 6px; letter-spacing: 1px; }
  .headline .tail { display: block; font-weight: 800; font-size: 52px; margin-top: 10px; letter-spacing: 0.5px; }
  .headline-pointer { position: absolute; left: 533px; top: 791px; width: 235px; height: 2px; background: var(--white); }
  .headline-pointer::after { content: ""; position: absolute; right: -5px; top: -4px; width: 10px; height: 10px; border-radius: 50%; background: var(--white); }
  .services { position: absolute; left: 0; top: 844px; width: 832px; display: flex; justify-content: center; }
  .service { width: 174px; text-align: center; }
  .service-icon {
    width: 76px; height: 76px; margin: 0 auto; border-radius: 50%;
    background: var(--white); border: 4px solid var(--brand-blue);
    display: flex; align-items: center; justify-content: center;
  }
  .service-title { margin-top: 20px; color: var(--brand-blue); font-weight: 700; font-size: 24px; }
  .service-text { margin-top: 4px; color: var(--text-grey); font-size: 12.5px; line-height: 1.35; }
  .contact { position: absolute; left: 0; top: 1038px; width: 832px; height: 162px; }
  .contact-phone { position: absolute; left: 60px; top: 40px; display: flex; align-items: center; gap: 8px;
    font-family: "Montserrat", sans-serif; font-weight: 700; font-size: 36px; }
  .contact-email { position: absolute; left: 60px; top: 87px; display: flex; align-items: center; gap: 9px;
    font-family: "Montserrat", sans-serif; font-weight: 400; font-size: 20px; }
  .contact-divider { position: absolute; left: 399px; top: 45px; width: 2px; height: 66px; background: var(--white); }
  .contact-address { position: absolute; left: 438px; top: 55px; display: flex; gap: 8px;
    font-family: "Montserrat", sans-serif; font-weight: 700; font-size: 22px; line-height: 1.4; }
</style>
</head>
<body>
  <div class="ad">
    <svg class="ad-shapes" width="832" height="1200" viewBox="0 0 832 1200">
      <defs>
        <linearGradient id="crowdTones" x1="0" y1="0" x2="1" y2="1">
          <stop offset="0" stop-color="#8e9a9c"/>
          <stop offset="0.45" stop-color="#6f7d78"/>
          <stop offset="0.7" stop-color="#7d6a62"/>
          <stop offset="1" stop-color="#a8b0ae"/>
        </linearGradient>
      </defs>
      <rect class="hero-photo" role="img" aria-label="Aerial photo of a large crowd gathered at a barricaded race start on a city street" x="0" y="0" width="832" height="650" fill="url(#crowdTones)"/>
      <polygon class="hero-shade" points="0,0 832,0 832,94 0,246" fill="#1c1d1e" fill-opacity="0.82"/>
      <polygon class="headline-panel" points="0,497 832,640 832,884 0,884" fill="var(--brand-blue)"/>
      <rect class="services-band" x="0" y="882" width="832" height="156" fill="var(--band-light)"/>
      <rect class="contact-band" x="0" y="1038" width="832" height="162" fill="var(--ink-dark)"/>
    </svg>

    <div class="brand"><span class="brand-dot"></span><span class="brand-name">Harbor Lane Partners</span></div>
    <div class="website">
      <svg width="14" height="14" viewBox="0 0 14 14" fill="none" stroke="#fff" stroke-width="1.3"><circle cx="7" cy="7" r="6"/><ellipse cx="7" cy="7" rx="2.6" ry="6"/><line x1="1" y1="7" x2="13" y2="7"/></svg>
      www.harborlanepartners.us
    </div>

    <div class="headline-rule"></div>
    <h1 class="headline">
      <span class="lead">Creating</span>
      <span class="key">Secure</span>
      <span class="tail">Environments</span>
    </h1>
    <div class="headline-pointer"></div>

    <div class="services">
      <div class="service">
        <div class="service-icon">
          <svg width="38" height="40" viewBox="0 0 38 40" fill="none" stroke="#2f78bb" stroke-width="1.8" stroke-linecap="round"><rect x="5" y="5" width="28" height="32" rx="2"/><line x1="12" y1="2" x2="12" y2="8"/><line x1="19" y1="2" x2="19" y2="8"/><line x1="26" y1="2" x2="26" y2="8"/><path d="M10 16l2 2 3-3M10 23l2 2 3-3M10 30l2 2 3-3"/><line x1="19" y1="17" x2="28" y2="17"/><line x1="19" y1="24" x2="28" y2="24"/><line x1="19" y1="31" x2="28" y2="31"/></svg>
        </div>
        <div class="service-title">PLAN</div>
        <div class="service-text">Security assessment and<br>planning services</div>
      </div>
      <div class="service">
        <div class="service-icon">
          <svg width="42" height="42" viewBox="0 0 42 42" fill="none" stroke="#2f78bb" stroke-width="1.8" stroke-linecap="round" stroke-linejoin="round"><path d="M18 4h6l1 5 4 2 4-3 4 4-3 4 2 4 5 1v6l-5 1-2 4 3 4-4 4-4-3-4 2-1 5h-6l-1-5-4-2-4 3-4-4 3-4-2-4-5-1v-6l5-1 2-4-3-4 4-4 4 3 4-2z"/><path d="M14 28l8-8a5 5 0 0 1 6-6l-3 3 1 2 2 1 3-3a5 5 0 0 1-6 6l-8 8z"/></svg>
        </div>
        <div class="service-title">DESIGN</div>
        <div class="service-text">Security design and<br>engineering</div>
      </div>
      <div class="service">
        <div class="service-icon">
          <svg width="40" height="40" viewBox="0 0 40 40" fill="none" stroke="#2f78bb" stroke-width="1.8" stroke-linecap="round" stroke-linejoin="round"><path d="M34 6c-9 0-16 6-20 16l4 4c10-4 16-11 16-20z"/><circle cx="26" cy="14" r="3"/><path d="M14 22l-6 1 4-6 6-1M18 26l-1 6 6-4 1-6"/><path d="M10 28l-5 5M13 31l-4 4M8 25l-4 3"/></svg>
        </div>
        <div class="service-title">DEPLOY</div>
        <div class="service-text">Procurement and Project<br>Management Services</div>
      </div>
      <div class="service">
        <div class="service-icon">
          <svg width="42" height="40" viewBox="0 0 42 40" fill="none" stroke="#2f78bb" stroke-width="1.8" stroke-linecap="round"><circle cx="21" cy="9" r="6"/><circle cx="10" cy="29" r="6"/><circle cx="32" cy="29" r="6"/><path d="M18 15l-5 8M24 15l5 8M16 29h10"/></svg>
        </div>
        <div class="service-title">MANAGE</div>
        <div class="service-text">Comprehensive security<br>program management</div>
      </div>
    </div>

    <div class="contact">
      <div class="contact-phone">
        <svg width="28" height="28" viewBox="0 0 28 28" fill="none" stroke="#2f78bb" stroke-width="2"><circle cx="14" cy="14" r="12"/><path d="M10 8l2 3-1.5 1.5a8 8 0 0 0 5 5L17 16l3 2-1 2.5c-5 0-11-6-11-11z" stroke-linejoin="round"/></svg>
        888-416-2057
      </div>
      <div class="contact-email">
        <svg width="26" height="18" viewBox="0 0 26 18" fill="none" stroke="#2f78bb" stroke-width="1.8"><rect x="1" y="1" width="24" height="16"/><path d="M1 1l12 9 12-9M1 17l9-8M25 17l-9-8"/></svg>
        info@harborlanepartners.us
      </div>
      <div class="contact-divider"></div>
      <div class="contact-address">
        <svg width="14" height="22" viewBox="0 0 14 22" fill="none" stroke="#2f78bb" stroke-width="1.8" style="margin-top:4px"><circle cx="7" cy="6" r="4.5"/><line x1="7" y1="10.5" x2="7" y2="18"/><path d="M2 19h10"/></svg>
        <span>82 Morrow Ave. Suite 615,<br>Alder Ridge, NJ 07413</span>
      </div>
    </div>
  </div>
</body>
</html>
```